Industry and Trade -may go complete production

Industrial and Corporate Clothing ecom and showcase web site
see supplier ref sites:
www.grondelgear.example.com.au
www.pellimarstitch.example.com/,
www.Qorwin.example.com.au
Our logo is a roundal shaped gear cog with an elephant inside it.
Main Objective

Get people to contact us for industrial and corporate wear
order online or contact us for more details on products

Information in seconday pages inmportant and ISO standards etc.
Primary Points:

Must show that we are strong and solid.
Visual imagery is important.
We have many web sites in line and this is a start, see bentmardispatch.example.com.au for one of ours.

We need a layout for the home page and internal pages. It's an ecomm retail site! Must sell the products AND our company.

Internal pages would be product description pages.

Each page must present an opportunity for them to contact us.
Updates

http://shop.zelkavision.example.com/clash-of-marrowdeep-a-fieldcraft-card-game/detail.php?p=471093&v=zkv_series_crowns-of-marrowdeep_games#tabs

has very good features 

Project Deadline Extended
Reason: Not Enough Responses. This will open up to a designer doing continuous designs for our company. We had lost our last in house designer and need a new innovative person to create genius.

Hi

This tender has been extended due to non response. 
This is our first look at the system as we had designers inder contract who have now left. There are may web sites etc to be done and this is more of a interview.

It is well worth responding. There are already 6 other projects in the pipline. But we want the best .
Garret de Vashmoor
Group COO Harbourline Dispatch Pty Ltd
Sydney Australia.

Target Market(s)

TARGET MARKET:
Tradesmen and Corporations and Government agencies
again see the above web sites they address the same markets
especially grondel.example.com.au

Industry/Entity Type

Industrial

Requirements
Must have
• Strength of company
supply and quality are important
ease of use, grondel.example.com.au can be used for good visual expression.
Nice to have
• extreme images and ease of use in navigation and contact.
look at imagery on grondel web site grondel.example.com.au
font useage: see http://money.quorvanews.example.com.au/newsbusiness/wpx/5139207/plendacom-signs-9b-fibre-agreement for font size usage. clear clean to the point.
Should not have
• kitch

```html
<!DOCTYPE html>
<html lang="en">
<head>
<meta charset="utf-8">
<title>Industry &amp; Trade</title>
<link rel="stylesheet" href="https://fonts.googleapis.com/css2?family=Cabin:wght@400;600;700&family=Arimo:ital,wght@0,400;1,400&family=Reenie+Beanie&display=swap">
<style>
:root{
  --navy:#1d2a5a;
  --navy-light:#2f437c;
  --orange:#f7a11d;
  --orange-light:#fbb93b;
  --text:#3d3d3d;
  --muted:#7a7a7a;
  --rule:#e3e3e3;
  --link-blue:#5aa6c9;
  --white:#ffffff;
}
*{margin:0;padding:0;box-sizing:border-box}
html,body{width:1200px;height:636px;overflow:hidden;background:var(--white)}
body{position:relative;font-family:Arimo,Arial,sans-serif;color:var(--text)}
.abs{position:absolute}

.header-rule{left:0;top:47px;width:1040px;height:1px;background:#eeeeee}
.brand{left:136px;top:12px;display:flex;align-items:center;gap:8px}
.brand-mark{width:40px;height:40px;border-radius:50%;background:var(--navy)}
.brand-name{font-family:Cabin,sans-serif;font-weight:700;font-size:20px;line-height:19px;color:var(--navy);width:110px}

.main-nav{left:371px;top:27px;display:flex;font-family:Cabin,sans-serif;font-size:12px;color:#333}
.main-nav span{display:flex;align-items:center;gap:6px}
.main-nav span::after{content:"";width:4px;height:4px;border-right:1px solid #aaa;border-bottom:1px solid #aaa;transform:rotate(45deg);margin-top:-3px}
.main-nav .current{color:var(--orange)}

.search{left:155px;top:93px;width:295px;height:30px;border-radius:8px;background:linear-gradient(#f7f7f7,#e9e9e9);box-shadow:inset 0 1px 2px rgba(0,0,0,.12);font-family:Arimo,sans-serif;font-style:italic;font-size:12px;color:#666;padding:9px 18px}
.search svg{position:absolute;right:10px;top:6px}

.hint{left:710px;top:86px;width:250px;font-family:"Reenie Beanie",cursive;font-size:23px;line-height:19px;color:#555}
.hint-arrow{left:960px;top:96px}
.slide-btn{top:155px;width:17px;height:17px;border-radius:50%;background:var(--navy);color:#fff;font-size:12px;line-height:15px;text-align:center;font-family:Arimo,sans-serif;z-index:3}

.panel{top:162px;height:208px;color:#fff}
.panel-about{left:129px;width:445px;border-radius:6px 0 0 6px;background:linear-gradient(var(--navy-light),var(--navy) 45%)}
.panel-clothing{left:570px;width:476px;border-radius:0 6px 6px 0;background:linear-gradient(var(--orange-light),var(--orange) 40%)}
.panel-title{position:absolute;top:15px;font-family:Cabin,sans-serif;font-weight:600;font-size:18px;text-shadow:0 1px 1px rgba(0,0,0,.2)}
.panel-rule{position:absolute;top:44px;left:0;right:0;height:1px;background:rgba(255,255,255,.15)}
.panel-body{position:absolute;top:50px;font-size:8.6px;line-height:14px;letter-spacing:-0.1px}
.panel-body p+p{margin-top:14px}
.read-more{position:absolute;top:164px;width:84px;height:28px;border-radius:5px;font-family:Cabin,sans-serif;font-weight:700;font-size:10.5px;text-align:center;line-height:28px;color:#fff}
.panel-about .read-more{left:230px;background:linear-gradient(var(--orange-light),var(--orange))}
.panel-clothing .read-more{left:352px;background:linear-gradient(var(--navy-light),var(--navy))}

.hero-photo{left:474px;top:75px;width:192px;height:295px;border-radius:0 0 96px 96px;background:linear-gradient(170deg,#dfe6f1,#a9bedc 50%,#6c7da0);z-index:2}

.col{top:370px;width:171px}
.col-bar{height:3px}
.col-title{font-family:Cabin,sans-serif;font-size:13px;padding:6px 14px 0;height:28px;border-bottom:1px solid #f4cf9f}
.col-news{left:133px}.col-news .col-bar{background:var(--orange)}.col-news .col-title{color:var(--orange)}
.col-products{left:398px}.col-products .col-bar{background:var(--orange)}.col-products .col-title{color:var(--orange)}
.col-catalogues{left:808px}.col-catalogues .col-bar{background:var(--navy)}.col-catalogues .col-title{color:var(--navy);border-bottom-color:#bbb}

.news-item{position:relative;height:36px;border-bottom:1px dashed #a9d2e3;font-size:8.5px;color:#555}
.news-item .icon{position:absolute;left:14px;top:9px}
.news-item .headline{position:absolute;left:38px;top:9px}
.news-item .headline::after{content:" \203A";color:var(--navy);font-size:10px;margin-left:4px}
.news-item .date{position:absolute;left:10px;top:21px;font-size:7.5px;color:var(--link-blue)}

.product{top:415px;width:132px;height:88px;border-radius:6px;overflow:hidden}
.product-label{position:absolute;left:50%;top:-30px;transform:translateX(-50%);width:118px;height:58px;border-radius:50%;background:#fff;font-family:Cabin,sans-serif;font-size:10px;color:#333;text-align:center;padding-top:34px}
.product-shirt{left:403px;background:linear-gradient(110deg,#c98d6b,#6f8fc9 45%,#7d9a6b 75%,#c4a3c8)}
.product-classic{left:584px;background:linear-gradient(110deg,#6b2a3e,#e36a95 50%,#c7b9c2)}

.catalogue-name{left:826px;top:412px;font-family:Cabin,sans-serif;font-size:13.5px;line-height:21px;color:#333}
.catalogue-file{left:929px;top:424px;width:38px;height:42px;border-radius:3px;background:linear-gradient(#f4f4f4,#d8d8d8);border:1px solid #bbb}
.catalogue-file::before{content:"";position:absolute;left:-3px;top:6px;width:22px;height:11px;background:#d52b1e;border-radius:2px}
.download{left:850px;top:462px;font-style:italic;font-size:10.5px;color:var(--navy);display:flex;align-items:center;gap:5px}

.footer-rule{left:128px;top:545px;width:1072px;height:1px;background:#dcdcdc}
.copyright{left:877px;top:554px;font-size:8.5px;color:var(--muted)}
</style>
</head>
<body>
<div class="abs header-rule"></div>
<div class="abs brand"><span class="brand-mark"></span><span class="brand-name">INDUSTRY &amp; TRADE</span></div>
<nav class="abs main-nav">
  <span style="width:78px">Home</span>
  <span class="current" style="width:93px">About us</span>
  <span style="width:93px">Products</span>
  <span style="width:91px">Services</span>
  <span style="width:96px">Materials</span>
  <span style="width:106px">Contact Us</span>
  <span>Shop</span>
</nav>

<div class="abs search">Search...
  <svg width="16" height="16" viewBox="0 0 16 16"><circle cx="6" cy="6" r="4" fill="none" stroke="#888" stroke-width="1.5"/><path d="M9 9l4 4" stroke="#888" stroke-width="2" stroke-linecap="round"/></svg>
</div>

<div class="abs hint">Use if you want to change the product</div>
<svg class="abs hint-arrow" width="46" height="46" viewBox="0 0 46 46"><path d="M4 3c20 0 30 12 38 38" fill="none" stroke="#777" stroke-width="1.3"/><path d="M33 34l9 7 1-11" fill="none" stroke="#777" stroke-width="1.3"/></svg>

<section class="abs panel panel-about">
  <h2 class="panel-title" style="left:28px">About Industry &amp; Trade</h2>
  <div class="panel-rule"></div>
  <div class="panel-body" style="left:28px;width:308px">
    <p>Contrary to popular belief, Lorem Ipsum is not simply random text. It has roots in a piece of classical Latin literature from 45 BC, making it over 2000 years old. Rowan Maddeley, a Latin professor at Harrowgate-Lynde College in Vermont, looked up one of the more obscure Latin words.</p>
    <p>Consectetur, from a Lorem Ipsum passage, and going through the cites of the word in classical literature, discovered the undoubtable source.<br>Lorem Ipsum comes...</p>
  </div>
  <div class="read-more">Read more</div>
</section>

<section class="abs panel panel-clothing">
  <h2 class="panel-title" style="left:127px">Corporate Clothing</h2>
  <div class="panel-rule"></div>
  <div class="panel-body" style="left:127px;width:312px">
    <p>There are many variations of passages of Lorem Ipsum available, but the majority have suffered alteration in some form, by injected humour, or randomised words which don't look even slightly believable.</p>
    <p>If you are going to use a passage of Lorem Ipsum, you need to be sure there isn't anything embarrassing hidden in the middle of text. All the Lorem Ipsum generators on the Internet tend to repeat predefined chunks as necessary, making this the first true generator on the Internet.</p>
  </div>
  <div class="read-more">Read more</div>
</section>

<div class="abs slide-btn" style="left:995px">&#8249;</div>
<div class="abs slide-btn" style="left:1012px">&#8250;</div>

<div class="abs hero-photo" role="img" aria-label="Smiling man in a blue striped business shirt giving a thumbs up"></div>

<section class="abs col col-news">
  <div class="col-bar"></div>
  <h3 class="col-title">Latest News</h3>
  <div class="news-item"><svg class="icon" width="12" height="10" viewBox="0 0 12 10"><path d="M1 1h10v6H5l-3 2V7H1z" fill="none" stroke="#777"/></svg><span class="headline">The Lindvale IPO</span><span class="date">22 may</span></div>
  <div class="news-item"><svg class="icon" width="12" height="10" viewBox="0 0 12 10"><path d="M1 1h10v6H5l-3 2V7H1z" fill="none" stroke="#777"/></svg><span class="headline">Industry &amp; Trade in live.</span><span class="date">19 may</span></div>
  <div class="news-item"><svg class="icon" width="12" height="10" viewBox="0 0 12 10"><path d="M1 1h10v6H5l-3 2V7H1z" fill="none" stroke="#777"/></svg><span class="headline">Will Quorbit destroy Wispnet?</span><span class="date">18 may</span></div>
</section>

<section class="abs col col-products">
  <div class="col-bar"></div>
  <h3 class="col-title">New Products</h3>
</section>
<div class="abs product product-shirt" role="img" aria-label="Folded business shirts in assorted colours"><div class="product-label">Shirt in grid</div></div>
<div class="abs product product-classic" role="img" aria-label="Pink and dark shirts hanging on a rail"><div class="product-label">Classic 2011</div></div>

<section class="abs col col-catalogues">
  <div class="col-bar"></div>
  <h3 class="col-title">Latest Catalogues</h3>
</section>
<div class="abs catalogue-name">Industry &amp; Trade<br>Catalogue 2011</div>
<div class="abs catalogue-file"></div>
<div class="abs download">Download <svg width="14" height="8" viewBox="0 0 14 8"><path d="M0 4h13M9 1l4 3-4 3" fill="none" stroke="#1d2a5a"/></svg></div>

<div class="abs footer-rule"></div>
<div class="abs copyright">All rights reserved. Industry &amp; trade 2011</div>
</body>
</html>
```